Telephony business needs eye-catching design for window cling advertisement

We need a design for an 8.5" x 6" window cling to place in Business Park developments. Can be horizontal or vertical layout.
Copy should read: 604-517-9482 (prominent)
Phones, phone lines, internet, security
60 days no-risk guarantee (seal design graphic)
We’re going to make a complete RISK FREE DECISION for you!
MORE SUPPORT, MORE SAVINGS, MORE PROFIT
Logo
RQVB.tel
Background info to keep in mind for design:
We are marketing internet access, phone systems, phone lines, security lines and cabling lines also fast turn-around time from initial contact to full operation. Our target client is 50 or less phone systems. We are uploading a promo piece we like for copy reference and our own logo.

Target Market(s)

new businesses, new business tenants under 50 people

Industry/Entity Type

Telecommunications

Font styles to use
Serif
Sans Serif

Requirements
Must have
• All copy listed, guarantee seal graphic
Nice to have
• Phone number prominence, our logo can be small
Should not have
• star bursts

```html
<!DOCTYPE html>
<html lang="en">
<head>
<meta charset="utf-8">
<title>RQVB 60 Days No-Risk Guarantee Window Cling</title>
<link rel="stylesheet" href="https://fonts.googleapis.com/css2?family=Arimo:ital,wght@0,400;0,700;1,700&family=Poppins:wght@600&display=swap">
<style>
  :root {
    --brand-red: #e3161c;
    --curtain-deep: #5e0407;
    --curtain-mid: #a50d12;
    --curtain-light: #d2231f;
    --panel-yellow: #ffde17;
    --gold-light: #fff2a8;
    --gold: #f2c230;
    --gold-dark: #b9851a;
    --ribbon-red: #c8151b;
    --ribbon-dark: #7e0a0e;
    --white: #ffffff;
  }
  * { margin: 0; padding: 0; box-sizing: border-box; }
  html, body { width: 846px; height: 1200px; overflow: hidden; background: #ffffff; }
  .cling {
    position: relative;
    width: 846px;
    height: 1200px;
    overflow: hidden;
    font-family: "Arimo", Arial, sans-serif;
    color: var(--white);
  }
  .stage-curtain {
    position: absolute; inset: 0;
    background:
      radial-gradient(ellipse 60% 45% at 50% 40%, rgba(255,120,80,0.35), rgba(0,0,0,0) 70%),
      linear-gradient(90deg, var(--curtain-deep) 0%, var(--curtain-mid) 18%, var(--curtain-light) 50%, var(--curtain-mid) 82%, var(--curtain-deep) 100%);
  }
  .phone-band {
    position: absolute; left: 0; top: 0;
    width: 846px; height: 153px;
    background: var(--panel-yellow);
    border-radius: 0 0 56px 56px;
    display: flex; align-items: center; justify-content: center;
  }
  .phone-number {
    font-weight: 700;
    font-size: 76px;
    letter-spacing: 1px;
    color: var(--brand-red);
  }
  .guarantee-seal {
    position: absolute; left: 0; top: 150px; width: 846px; height: 540px;
  }
  .seal-disc { position: absolute; left: 0; top: 0; }
  .seal-number {
    position: absolute; left: 0; width: 846px; top: 88px;
    text-align: center;
    font-family: "Poppins", Arial, sans-serif;
    font-weight: 600;
    font-size: 230px;
    line-height: 1;
    letter-spacing: -8px;
    color: var(--white);
    -webkit-text-stroke: 6px var(--gold);
    paint-order: stroke fill;
    text-shadow: 0 6px 10px rgba(90,40,0,0.45);
  }
  .seal-days {
    position: absolute; left: 344px; top: 318px;
    width: 158px; height: 50px;
    border-radius: 25px;
    background: linear-gradient(180deg, var(--gold-light), var(--gold) 55%, var(--gold-dark));
    border: 3px solid var(--white);
    text-align: center;
    font-family: "Poppins", Arial, sans-serif;
    font-weight: 600; font-size: 32px; line-height: 44px;
    color: var(--white);
    text-shadow: 0 1px 2px rgba(120,60,0,0.6);
  }
  .seal-ribbon { position: absolute; left: 0; top: 380px; }
  .seal-norisk {
    position: absolute; left: 0; width: 846px; top: 398px;
    text-align: center;
    font-weight: 700; font-size: 60px; line-height: 66px; letter-spacing: 3px;
  }
  .seal-guarantee {
    position: absolute; left: 0; width: 846px; top: 472px;
    text-align: center;
    font-weight: 700; font-size: 23px; line-height: 26px; letter-spacing: 9px;
  }
  .promise {
    position: absolute; left: 0; width: 846px; top: 728px;
    text-align: center;
  }
  .promise-lead { font-size: 35px; letter-spacing: 1px; line-height: 44px; }
  .promise-strong { font-size: 38px; font-weight: 700; line-height: 50px; }
  .promise-strong span { font-weight: 400; font-size: 35px; }
  .services-bar {
    position: absolute; left: 78px; top: 836px;
    width: 690px; height: 44px;
    background: var(--panel-yellow);
    display: flex; align-items: center; justify-content: center;
    font-size: 31px; color: var(--brand-red);
  }
  .services-chevrons { position: absolute; top: 832px; }
  .services-chevrons.left { left: 62px; }
  .services-chevrons.right { left: 730px; }
  .benefits {
    position: absolute; left: 0; width: 846px; top: 896px;
    text-align: center;
    font-weight: 700; font-style: italic;
    font-size: 38px; line-height: 48px;
  }
  .logo-panel {
    position: absolute; left: 0; top: 1012px;
    width: 846px; height: 188px;
    background: var(--panel-yellow);
    border-radius: 56px 56px 0 0;
    display: flex; flex-direction: column; align-items: center; justify-content: center;
    color: var(--brand-red);
    font-weight: 700;
  }
  .brand-mark {
    display: flex; align-items: center; gap: 14px;
  }
  .brand-dot {
    width: 36px; height: 36px; border-radius: 50%;
    background: var(--brand-red);
  }
  .brand-name { font-size: 66px; line-height: 70px; letter-spacing: 2px; }
  .brand-full { font-size: 19px; line-height: 26px; letter-spacing: 5px; margin-top: 4px; }
  .brand-web { font-size: 28px; line-height: 34px; letter-spacing: 1px; margin-top: 2px; }
</style>
</head>
<body>
<main class="cling">
  <div class="stage-curtain" role="img" aria-label="Red theatre stage curtain backdrop"></div>

  <header class="phone-band">
    <p class="phone-number">604-517-9482</p>
  </header>

  <section class="guarantee-seal" aria-label="60 days no-risk guarantee seal">
    <svg class="seal-disc" width="846" height="540" viewBox="0 0 846 540" aria-hidden="true">
      <defs>
        <radialGradient id="sealGold" cx="50%" cy="40%" r="60%">
          <stop offset="0%" stop-color="#fff1a6"/>
          <stop offset="55%" stop-color="#e7b53a"/>
          <stop offset="100%" stop-color="#a87418"/>
        </radialGradient>
      </defs>
      <circle cx="423" cy="240" r="205" fill="url(#sealGold)"/>
      <circle cx="423" cy="240" r="182" fill="none" stroke="#fff6c8" stroke-width="4" stroke-dasharray="2 12" stroke-linecap="round"/>
    </svg>
    <div class="seal-number">60</div>
    <div class="seal-days">days</div>
    <svg class="seal-ribbon" width="846" height="140" viewBox="0 0 846 140" aria-hidden="true">
      <polygon fill="var(--ribbon-dark)" points="150,40 222,40 222,120 150,120 176,80"/>
      <polygon fill="var(--ribbon-dark)" points="696,40 624,40 624,120 696,120 670,80"/>
      <path fill="var(--ribbon-red)" stroke="#f2c230" stroke-width="3"
        d="M205,20 Q423,-8 641,20 L641,130 Q423,102 205,130 Z"/>
    </svg>
    <div class="seal-norisk">NO-RISK</div>
    <div class="seal-guarantee">GUARANTEE</div>
  </section>

  <section class="promise">
    <p class="promise-lead">We’re going to make a complete</p>
    <p class="promise-strong">RISK FREE DECISION <span>for you!</span></p>
  </section>

  <svg class="services-chevrons left" width="54" height="52" viewBox="0 0 54 52" aria-hidden="true">
    <polygon fill="var(--panel-yellow)" points="0,0 12,0 30,26 12,52 0,52 18,26"/>
    <polygon fill="var(--panel-yellow)" points="20,0 32,0 50,26 32,52 20,52 38,26"/>
  </svg>
  <p class="services-bar">Phones, phone lines, internet, security</p>
  <svg class="services-chevrons right" width="54" height="52" viewBox="0 0 54 52" aria-hidden="true">
    <polygon fill="var(--panel-yellow)" points="54,0 42,0 24,26 42,52 54,52 36,26"/>
    <polygon fill="var(--panel-yellow)" points="34,0 22,0 4,26 22,52 34,52 16,26"/>
  </svg>

  <p class="benefits">MORE SUPPORT, MORE SAVINGS,<br>MORE PROFIT</p>

  <footer class="logo-panel">
    <div class="brand-mark">
      <span class="brand-dot" aria-hidden="true"></span>
      <p class="brand-name">RQVB</p>
    </div>
    <p class="brand-full">RQVB VOICE BUREAU INC</p>
    <p class="brand-web">RQVB.tel</p>
  </footer>
</main>
</body>
</html>
```